Brackwell HVAC Service LLC Business Card

We just got a design created by one of your designers for a logo and now would like help with a business card design. The information to be included on the card is as follows:
Brackwell HVAC Service LLC (I will attach logo design)
P.O. Box 418
Cedar Ridge, KS 67490
(620) 555-0147
Dale Vonnholt
I might include an e-mail address, but I'm not sure yet.
Target Market(s)
Customers needing service or repairs done on their heating and air conditioning systems.
Industry/Entity Type
Business
Contact Information for Business Card
P.O. Box 418
Cedar Ridge, KS 67490
(620) 555-0147
Dale Vonnholt

```html
<!DOCTYPE html>
<html lang="en">
<head>
<meta charset="utf-8">
<title>Brackwell HVAC Service LLC – Business Card</title>
<link rel="stylesheet" href="https://fonts.googleapis.com/css2?family=Exo+2:wght@500&family=Open+Sans:wght@400;700&display=swap">
<style>
  :root {
    --backdrop: #e4e5e7;
    --card: #ffffff;
    --navy: #34558a;
    --red: #cf3a40;
    --ink: #2f3033;
    --muted: #4a4c50;
    --faint: rgba(52, 85, 138, 0.10);
  }
  html, body {
    margin: 0;
    padding: 0;
    width: 1200px;
    height: 871px;
    overflow: hidden;
    background: var(--backdrop);
  }
  .canvas {
    position: relative;
    width: 1200px;
    height: 871px;
  }
  .card {
    position: absolute;
    width: 600px;
    height: 343px;
    background: var(--card);
    box-shadow: 0 6px 18px rgba(0, 0, 0, 0.18);
    overflow: hidden;
  }
  .card--back { left: 80px; top: 70px; }
  .card--front { left: 520px; top: 450px; }

  .brand {
    position: absolute;
    display: flex;
    align-items: center;
    gap: 14px;
  }
  .brand__dot {
    border-radius: 50%;
    background: var(--red);
    flex: none;
  }
  .brand__name {
    font-family: "Open Sans", sans-serif;
    font-weight: 700;
    color: var(--navy);
    text-transform: uppercase;
    letter-spacing: 0.5px;
    line-height: 1.05;
  }
  .card--back .brand { left: 90px; top: 138px; }
  .card--back .brand__dot { width: 62px; height: 62px; }
  .card--back .brand__name { font-size: 27px; }

  .card--front .brand { left: 44px; top: 36px; }
  .card--front .brand__dot { width: 44px; height: 44px; }
  .card--front .brand__name { font-size: 19px; }

  .decor-ring {
    position: absolute;
    right: -70px;
    bottom: -90px;
    width: 300px;
    height: 300px;
    border-radius: 50%;
    background: var(--faint);
  }

  .holder {
    position: absolute;
    left: 44px;
    top: 138px;
    margin: 0;
    font-family: "Exo 2", sans-serif;
    font-weight: 500;
    font-size: 24px;
    letter-spacing: 4px;
    text-transform: uppercase;
    color: var(--ink);
  }
  .contact {
    position: absolute;
    left: 44px;
    top: 190px;
    margin: 0;
    font-family: "Open Sans", sans-serif;
    font-size: 15px;
    color: var(--muted);
    font-style: normal;
    line-height: 1.9;
  }
  .contact__phone {
    display: flex;
    align-items: center;
    gap: 10px;
  }
  .contact__icon { width: 16px; height: 16px; fill: var(--navy); }
</style>
</head>
<body>
  <main class="canvas">
    <section class="card card--back" aria-label="Card back">
      <div class="brand">
        <span class="brand__dot"></span>
        <span class="brand__name">Brackwell HVAC<br>Service LLC</span>
      </div>
    </section>

    <section class="card card--front" aria-label="Card front">
      <div class="decor-ring" role="img" aria-label="Faint brand emblem decoration"></div>
      <div class="brand">
        <span class="brand__dot"></span>
        <span class="brand__name">Brackwell HVAC<br>Service LLC</span>
      </div>
      <h1 class="holder">Dale Vonnholt</h1>
      <address class="contact">
        <div class="contact__address">P.O. Box 418&nbsp;&nbsp;Cedar Ridge, KS 67490</div>
        <div class="contact__phone">
          <svg class="contact__icon" viewBox="0 0 24 24" aria-hidden="true">
            <path d="M6.6 10.8a15.1 15.1 0 0 0 6.6 6.6l2.2-2.2a1 1 0 0 1 1-.25 11.4 11.4 0 0 0 3.6.57 1 1 0 0 1 1 1V20a1 1 0 0 1-1 1A17 17 0 0 1 3 4a1 1 0 0 1 1-1h3.5a1 1 0 0 1 1 1c0 1.25.2 2.46.57 3.6a1 1 0 0 1-.25 1z"/>
          </svg>
          <span>(620) 555-0147</span>
        </div>
      </address>
    </section>
  </main>
</body>
</html>
```